integrative health clinic-Medical massage, acupuncture, chiropractic

we like our logo, but are open to new ideas. We need a new card design. We have added chiropractic and acupuncture that we have put under the name of the business. We are an integrative medical clinic

Target Market(s)

General public, athletes

Contact Information for Business Card

Phone 5055583927
Fax 5055583926
Hours Monday-Friday 9-6
Saturday 10-6
The 20% can be smaller on the back

Colors
3176b5
0355a3

Requirements
Must have
• Logo but am open to ideas
Nice to have
• We are an integrated medical clinic but also want to be personable. We want the card fun and inviting

```html
<!DOCTYPE html>
<html lang="en">
<head>
<meta charset="utf-8">
<title>Evenfield Wellness – Business Card</title>
<link href="https://fonts.googleapis.com/css2?family=Open+Sans:wght@400;600&family=PT+Sans+Narrow:wght@700&family=Montserrat:wght@700&display=swap" rel="stylesheet">
<style>
  :root {
    --backdrop: #141415;
    --card: #232324;
    --brand-blue: #1f6fc0;
    --brand-deep: #0355a3;
    --name-violet: #3b40b3;
    --text-light: #e9e9ea;
    --pattern-light: #5a5a5c;
    --pattern-mid: #3a3a3c;
  }
  * { box-sizing: border-box; margin: 0; padding: 0; }
  html, body { width: 1200px; height: 780px; overflow: hidden; }
  body {
    background: var(--backdrop);
    position: relative;
    font-family: "Open Sans", sans-serif;
    color: var(--text-light);
  }
  .card {
    position: absolute;
    width: 540px;
    height: 310px;
    border-radius: 22px;
    background: var(--card);
    overflow: hidden;
  }
  .card--back { left: 60px; top: 60px; }
  .card--front { left: 600px; top: 410px; }

  .back-pattern {
    position: absolute;
    inset: 0;
    background:
      radial-gradient(ellipse at 30% 10%, var(--pattern-light) 0%, transparent 55%),
      linear-gradient(160deg, var(--pattern-mid) 0%, var(--card) 75%);
  }

  .brand {
    position: absolute;
    display: flex;
    align-items: flex-start;
    gap: 10px;
  }
  .brand__mark {
    width: 26px; height: 26px;
    border-radius: 50%;
    background: var(--brand-blue);
    margin-top: 10px;
    flex: none;
  }
  .brand__name {
    font-family: "PT Sans Narrow", sans-serif;
    font-weight: 700;
    font-size: 44px;
    line-height: 1;
    color: var(--brand-blue);
    letter-spacing: -0.5px;
  }
  .brand__tagline {
    font-family: "Open Sans", sans-serif;
    font-size: 15px;
    color: var(--brand-blue);
    margin-top: 4px;
    margin-left: 40px;
  }
  .card--back .brand { left: 34px; bottom: 42px; }
  .card--front .brand { left: 34px; top: 34px; }

  .person {
    position: absolute;
    right: 44px;
    top: 130px;
    text-align: right;
  }
  .person__name {
    font-family: "Montserrat", sans-serif;
    font-weight: 700;
    font-size: 30px;
    color: var(--name-violet);
    line-height: 1;
  }
  .person__role {
    font-size: 11px;
    letter-spacing: 0.5px;
    margin-top: 3px;
  }
  .accent-bar {
    position: absolute;
    right: 20px;
    top: 128px;
    width: 10px;
    height: 40px;
    background: var(--name-violet);
  }
  .divider {
    position: absolute;
    left: 0; right: 0;
    top: 190px;
    height: 2px;
    background: var(--name-violet);
  }
  .contact {
    position: absolute;
    left: 34px;
    top: 220px;
    font-size: 13px;
    line-height: 1.5;
    letter-spacing: 0.6px;
  }
  .hours {
    position: absolute;
    right: 34px;
    top: 206px;
    font-size: 12.5px;
    line-height: 1.5;
    text-align: right;
    letter-spacing: 0.5px;
  }
</style>
</head>
<body>

<section class="card card--back">
  <div class="back-pattern" role="img" aria-label="Repeating pattern of the clinic's emblem in grey tones, fading toward the lower right"></div>
  <div class="brand">
    <span class="brand__mark"></span>
    <div>
      <div class="brand__name">Evenfield Wellness</div>
      <div class="brand__tagline">Sports Therapy and Wellness Center</div>
    </div>
  </div>
</section>

<section class="card card--front">
  <div class="brand">
    <span class="brand__mark"></span>
    <div>
      <div class="brand__name">Evenfield Wellness</div>
      <div class="brand__tagline">Sports Therapy and Wellness Center</div>
    </div>
  </div>

  <div class="accent-bar"></div>
  <div class="person">
    <div class="person__name">MARA ELLIS</div>
    <div class="person__role">CEO &amp; FOUNDER</div>
  </div>

  <div class="divider"></div>

  <div class="contact">
    <p>Phone 5055583927</p>
    <p>Fax 5055583926</p>
  </div>

  <div class="hours">
    <p>Hours Monday-Friday 9-6</p>
    <p>Saturday 10-6</p>
  </div>
</section>

</body>
</html>
```